Business Card Design Project

Brightfern Consulting is a newly created boutique consultancy focussing on delivering strategic consulting to medium and large businesses, with a focus on:
- Strategic planning and execution.
- Corporate function optimisation, especially in the areas of finance, commercial, and IT. This includes implementing the right functional design for the needs of the business, and ensuring the right skills.
- Performance management, in particular project governance and control, operational metrics and management reporting.
I have in mind a tag line for the business being:
"Helping business to discover sustainable value."
I am looking for a letterhead design which utilises my new logo on report templates (powerpoint and word), and letterhead.
Trivopedix defines a mother lode as follows:
"Mother lode is a principal vein or zone of veins of gold or silver ore. The term probably came from a literal translation of the Spanish veta madre, a term common in old Mexican mining. Veta madre, for instance, is the name given to an 11-kilometre-long (6.8 mi) silver vein discovered in 1548 in Guanajuato, New Spain (modern-day Mexico)."
My preference is for black and gold. Logo files are attached in .eps format. All fonts are outlined. The fonts that are used are "Crimson Text" and "Josefin Sans". They are free open source fonts and they are available here: http://www.typevault.example/fonts
Target Market(s)
Medium to large corporates.
Industry/Entity Type
Boutique
Font styles to use
Other font styles liked:
- All Fonts Are Outlined. The Fonts That Are Used Are "Crimson Text" And "Josefin Sans". They Are Free Open Source Fonts And They Are Available Here: Http://www.typevault.example/fonts
Look and feel
Each slider illustrates characteristics of the customer's brand and the style your logo design should communicate.

```html
<!DOCTYPE html>
<html lang="en">
<head>
<meta charset="utf-8">
<title>Brightfern Consulting — Business Card</title>
<link rel="stylesheet" href="https://fonts.googleapis.com/css2?family=Crimson+Text:wght@400;600&display=swap">
<style>
  :root {
    --ink: #0b0b0b;
    --gold: #e0a52a;
    --white: #f4f4f4;
    --stage: #cfcfcf;
  }
  * { margin: 0; padding: 0; box-sizing: border-box; }
  html, body { width: 1200px; height: 926px; overflow: hidden; }
  body { background: var(--stage); position: relative; font-family: "Crimson Text", Georgia, serif; }

  .card {
    position: absolute;
    left: 220px;
    width: 760px;
    height: 420px;
    background: var(--ink);
    box-shadow: 0 6px 18px rgba(0,0,0,0.25);
    overflow: hidden;
  }
  .card-front { top: 28px; }
  .card-back  { top: 478px; }

  /* Front */
  .front-name {
    position: absolute; left: 0; right: 0; top: 180px;
    text-align: center; white-space: nowrap;
    color: var(--white); font-size: 52px; font-weight: 400; line-height: 1;
  }

  /* Back */
  .gold-band { position: absolute; left: 0; right: 0; bottom: 0; height: 52px; background: var(--gold); }
  .divider { position: absolute; left: 262px; width: 3px; background: var(--white); }
  .divider-top { top: 0; height: 78px; }
  .divider-bottom { top: 118px; bottom: 70px; }

  .mini-name {
    position: absolute; left: 18px; width: 230px; top: 60px;
    text-align: center; white-space: nowrap;
    color: var(--white); font-size: 22px; font-weight: 400; line-height: 1;
  }

  .holder { position: absolute; left: 18px; width: 224px; top: 172px; text-align: right; }
  .holder-name { color: var(--gold); font-size: 30px; line-height: 1; text-transform: uppercase; white-space: nowrap; }
  .holder-role { color: var(--gold); font-size: 13px; font-weight: 600; letter-spacing: 1px; text-transform: uppercase; margin-top: 6px; }

  .details { position: absolute; left: 290px; top: 80px; right: 24px; }
  .company { color: var(--gold); font-size: 31px; line-height: 1; margin-bottom: 40px; white-space: nowrap; }
  .address, .contacts { color: var(--white); font-size: 17px; line-height: 1.3; letter-spacing: 0.4px; white-space: nowrap; }
  .address { margin-bottom: 12px; }
</style>
</head>
<body>

  <section class="card card-front">
    <div class="front-name">Brightfern Consulting</div>
  </section>

  <section class="card card-back">
    <div class="mini-name">Brightfern Consulting</div>

    <div class="divider divider-top"></div>
    <div class="divider divider-bottom"></div>

    <div class="holder">
      <div class="holder-name">Alex Marlow</div>
      <div class="holder-role">Director</div>
    </div>

    <div class="details">
      <div class="company">Brightfern Consulting</div>
      <p class="address">Level 14, 88 Harrowgate Street,<br>Melbourne, VIC 3000, AUSTRALIA</p>
      <p class="contacts">
        m: +61 400 218 553 &nbsp;|&nbsp; p: +61 3 9018 4420<br>
        f: +61 3 9018 4421<br>
        w: brightfernconsulting.example<br>
        e: alex.marlow@brightfernconsulting.example
      </p>
    </div>

    <div class="gold-band"></div>
  </section>

</body>
</html>
```